Retail Sign for Houseplant Campaign

Sign will measure 3 to 4 foot tall by 22.2inches and place on rolling racks of houseplants for a retail promotion in The Brickfield Yard. The theme of the promotion will be "New Year, New You!" Selling points which should be on the sign are Houseplants give you a taste of nature, Houseplants boost air quality inside your home, Indoor plants reduce anxiety, Indoor plants make you more productive, Houseplants improve your concentration and memory.
Updates

Target Market(s)

People who love plants

Industry/Entity Type

Horticulture/ retail

Colors
00AB8E
00BBA5
67D7C9
C6EFE9
E9F9F6
59FF00
82FF00
B8FF75
E3FFCB
F4FFEA
FFF300
FFF600
FEFA6F
FFFEC7
FFFEE8

Requirements
Must have
• Must feel energetic and encourage people to buy plants. Should include 1-2 photos and the selling points listed

```html
<!DOCTYPE html>
<html lang="en">
<head>
<meta charset="UTF-8">
<title>New Year, New You! – Houseplant Promotion Sign</title>
<link href="https://fonts.googleapis.com/css2?family=Abel&family=Courgette&display=swap" rel="stylesheet">
<style>
  :root {
    --page-bg: #e4e6e6;
    --stripe-1: #13a3a2;
    --stripe-2: #17b2b0;
    --stripe-3: #6dd3cf;
    --stripe-4: #a9e4e2;
    --header-teal: #2ac3c3;
    --points-panel: #b2e4e3;
    --brand-panel: #f4f6f6;
    --brand-green: #2f4a2a;
    --text-dark: #1d2b2b;
    --white: #ffffff;
  }
  * { box-sizing: border-box; margin: 0; padding: 0; }
  html, body {
    width: 1200px; height: 1000px; overflow: hidden;
    background: var(--page-bg);
  }
  .canvas {
    position: relative; width: 1200px; height: 1000px;
  }
  .sign {
    position: absolute; left: 375px; top: 28px;
    width: 450px; height: 943px;
    display: flex; flex-direction: column;
    box-shadow: 0 10px 30px rgba(0,0,0,0.18);
    background: var(--white);
  }
  .stripe-band { display: flex; height: 25px; flex: none; }
  .stripe-band span { flex: 1; }
  .stripe-band .s1 { background: var(--stripe-1); }
  .stripe-band .s2 { background: var(--stripe-2); }
  .stripe-band .s3 { background: var(--stripe-3); }
  .stripe-band .s4 { background: var(--stripe-4); }

  .headline-panel {
    height: 198px; flex: none;
    background: var(--header-teal);
    color: var(--white);
    font-family: "Courgette", cursive;
    font-size: 52px; line-height: 1.05;
    padding: 40px 0 0 48px;
  }
  .headline-panel .line-2 { display: block; padding-left: 62px; }

  .hero-photo {
    height: 330px; flex: none;
    background: linear-gradient(120deg, #efe9e1 0%, #d9d3ca 35%, #7fa3a0 60%, #4f6e45 85%, #8fa88a 100%);
  }
  .thumb-row {
    height: 111px; flex: none;
    display: flex; gap: 3px;
  }
  .thumb { flex: 1; }
  .thumb-1 { background: linear-gradient(135deg, #e9e2d4, #c7a68c 55%, #6f8f58); }
  .thumb-2 { background: linear-gradient(135deg, #f1eee8, #9fb88a 45%, #d9b8c0); }
  .thumb-3 { background: linear-gradient(135deg, #f2f0ec, #d7c6b8 50%, #4e8a46); }

  .selling-points {
    height: 158px; flex: none;
    background: var(--points-panel);
    font-family: "Abel", sans-serif;
    color: var(--text-dark);
    font-size: 16.5px; line-height: 24px;
    text-align: center;
    list-style: none;
    padding-top: 18px;
  }

  .brand-panel {
    height: 97px; flex: none;
    background: var(--brand-panel);
    display: flex; align-items: center; justify-content: center; gap: 12px;
  }
  .brand-mark { width: 38px; height: 38px; background: var(--brand-green); }
  .brand-name {
    font-family: "Abel", sans-serif;
    color: var(--brand-green);
    font-size: 36px; letter-spacing: 1px;
  }
</style>
</head>
<body>
<div class="canvas">
  <article class="sign">
    <div class="stripe-band"><span class="s1"></span><span class="s2"></span><span class="s3"></span><span class="s4"></span></div>

    <header class="headline-panel">
      <h1 style="font-weight:400;font-size:inherit;">"New Year,<span class="line-2">New You!"</span></h1>
    </header>

    <div class="hero-photo" role="img" aria-label="Photo of a mother and young daughter watering a snake plant in a green ceramic pot with a turquoise watering can"></div>

    <div class="thumb-row">
      <div class="thumb thumb-1" role="img" aria-label="Photo of a woman tending potted plants on a shelf"></div>
      <div class="thumb thumb-2" role="img" aria-label="Photo of a woman relaxing on a sofa surrounded by houseplants"></div>
      <div class="thumb thumb-3" role="img" aria-label="Photo of a smiling woman wiping the leaves of a monstera plant"></div>
    </div>

    <ul class="selling-points">
      <li>Houseplants give you a taste of nature.</li>
      <li>Houseplants boost air quality inside your home.</li>
      <li>Indoor plants reduce anxiety.</li>
      <li>Indoor plants make you more productive.</li>
      <li>Houseplants improve your concentration and memory.</li>
    </ul>

    <footer class="brand-panel">
      <span class="brand-mark"></span>
      <span class="brand-name">VERDANT LIVING</span>
    </footer>

    <div class="stripe-band"><span class="s1"></span><span class="s2"></span><span class="s3"></span><span class="s4"></span></div>
  </article>
</div>
</body>
</html>
```